Venture firm needs flyer to attract Sales Professionals as Advisors

Creation of either a pdf Flyer or Brochure.
The target audience are senior sales professionals of the Information Technology industry. The flyer needs to come across highly professional, business oriented, positive. Text for the brochure is attached. The colors/graphics should align with Brindmore Capital corporate appearance: www.brindmore.capital

Target Market(s)

Sales Professionals in the Information Technology Industry

Industry/Entity Type

Information Technology

Font styles to use
• Raleway

Requirements
Must have
• fitting the corporate look and feel: www.brindmore.capital

```html
<!DOCTYPE html>
<html lang="en">
<head>
<meta charset="utf-8">
<title>Brindmore Capital – Sales Council Flyer</title>
<link rel="stylesheet" href="https://fonts.googleapis.com/css2?family=Oswald:wght@500;600&family=Raleway:wght@300;400;500;600&display=swap">
<style>
:root{
  --page:#e8e5e0;
  --frame:#121418;
  --navy:#163f6e;
  --navy-deep:#0f2f56;
  --blue:#1b5d9c;
  --sky:#3b9ad9;
  --sky-light:#5cb1e6;
  --paper:#f4f5f7;
  --ink:#3a4756;
  --white:#ffffff;
}
*{margin:0;padding:0;box-sizing:border-box}
html,body{width:1200px;height:1200px;overflow:hidden;background:var(--page)}
body{font-family:"Raleway",sans-serif;position:relative}
.flyer{position:absolute;left:178px;top:15px;width:844px;height:1170px;background:var(--frame);padding:20px 22px}
.sheet{position:relative;width:800px;height:1130px;background:var(--paper);overflow:hidden}
.art{position:absolute;left:0;top:0}
.brand-top{position:absolute;left:14px;top:20px;color:var(--white);font-weight:400;font-size:33px;letter-spacing:.5px}
.headline{position:absolute;left:60px;top:310px;width:740px;height:45px;display:flex;align-items:center;justify-content:center;font-family:"Oswald",sans-serif;font-weight:500;font-size:34px;color:var(--white);letter-spacing:.3px}
.intro{position:absolute;left:13px;top:536px;width:778px}
.intro h2{font-family:"Oswald",sans-serif;font-weight:500;font-size:33px;line-height:40px;color:var(--sky);text-align:center;margin-bottom:4px;letter-spacing:.3px}
.intro p{font-size:14px;line-height:18px;color:var(--ink);font-weight:400;margin-bottom:5px}
.intro b{color:var(--navy-deep);font-weight:600}
.card{position:absolute;top:772px;width:248px;height:245px;background:var(--sky);color:var(--white);padding:90px 10px 0}
.card-icon{position:absolute;left:50%;top:-43px;width:86px;height:86px;margin-left:-43px;border-radius:50%;background:var(--white);display:flex;align-items:center;justify-content:center}
.card-icon span{width:74px;height:74px;border-radius:50%;background:var(--sky);border:3px solid var(--navy);display:flex;align-items:center;justify-content:center}
.card h3{position:absolute;left:0;right:0;top:55px;text-align:center;font-family:"Oswald",sans-serif;font-weight:500;font-size:18px}
.card h3 u{text-decoration:none;border-bottom:2px solid var(--white);padding:0 2px 1px}
.card p{font-size:9px;line-height:11px;text-align:justify;font-weight:400}
.card-how{left:12px}.card-assoc{left:274px}.card-adv{left:536px}
.rule{position:absolute;left:0;top:1024px;width:800px;height:4px;background:var(--sky)}
.footer{position:absolute;left:0;top:1033px;width:800px;height:97px;background:linear-gradient(90deg,var(--navy-deep),var(--blue) 50%,var(--navy-deep));color:var(--white);font-size:12.5px}
.office{position:absolute;top:10px}
.office h4{font-family:"Oswald",sans-serif;font-weight:500;font-size:16.5px;margin-bottom:10px;display:inline-block;border-bottom:1px solid var(--white)}
.office li{list-style:none;line-height:16px;display:flex;align-items:center;gap:5px}
.office-usa{left:14px}
.office-eu{right:13px;text-align:right}
.office-eu li{justify-content:flex-end}
.footer-brand{position:absolute;left:292px;top:35px;width:222px;height:40px;border:2px solid var(--white);border-radius:10px;display:flex;align-items:center;justify-content:center;font-size:19px;font-weight:400;letter-spacing:.5px}
</style>
</head>
<body>
<div class="flyer">
  <div class="sheet">
    <svg class="art" width="800" height="530" viewBox="0 0 800 530">
      <defs>
        <linearGradient id="sky" x1="0" y1="0" x2="1" y2="1">
          <stop offset="0" stop-color="#c9ced4"/><stop offset=".5" stop-color="#e9ecef"/><stop offset="1" stop-color="#6d6a66"/>
        </linearGradient>
        <linearGradient id="snow" x1="0" y1="0" x2="0" y2="1">
          <stop offset="0" stop-color="#b8c0cc"/><stop offset="1" stop-color="#eef1f5"/>
        </linearGradient>
        <linearGradient id="race" x1="0" y1="0" x2="1" y2="0">
          <stop offset="0" stop-color="#9aa4b2"/><stop offset=".5" stop-color="#b3545c"/><stop offset="1" stop-color="#c9ccd3"/>
        </linearGradient>
        <linearGradient id="band" x1="0" y1="0" x2="1" y2="0">
          <stop offset="0" stop-color="#1c5d9a"/><stop offset="1" stop-color="#123e6e"/>
        </linearGradient>
      </defs>
      <g role="img" aria-label="Photo: two climbers helping each other onto a rock summit above snowy mountains">
        <rect x="0" y="0" width="800" height="300" fill="url(#sky)"/>
      </g>
      <polygon points="0,0 425,0 367,83 0,83" fill="url(#band)"/>
      <polygon points="800,85 800,150 722,300 682,300" fill="#3b9ad9"/>
      <polygon points="800,195 800,300 745,300" fill="#1b5d9c"/>
      <rect x="0" y="300" width="800" height="230" fill="#f4f5f7"/>
      <polygon points="0,310 75,310 45,355 0,355" fill="#5cb1e6"/>
      <polygon points="90,310 800,310 800,330 785,355 60,355" fill="url(#band)"/>
      <polygon points="0,360 90,360 0,495" fill="#5cb1e6"/>
      <g role="img" aria-label="Photo: mountaineer standing on a snowy ridge">
        <polygon points="100,360 322,360 228,505 8,505" fill="url(#snow)"/>
      </g>
      <g role="img" aria-label="Photo: race car pit crew in motion">
        <polygon points="330,360 540,360 447,505 236,505" fill="url(#race)"/>
      </g>
      <g role="img" aria-label="Photo: hiker crossing a snowy mountain valley">
        <polygon points="548,360 760,360 667,505 455,505" fill="url(#snow)"/>
      </g>
      <polygon points="800,378 800,445 762,505 690,505" fill="#3b9ad9"/>
      <polygon points="10,513 800,513 793,524 0,524" fill="#163f6e"/>
    </svg>

    <div class="brand-top">BRINDMORE CAPITAL</div>
    <div class="headline">INVESTING IN GLOBAL GO-TO-MARKET STRATEGIES</div>

    <section class="intro">
      <h2>BRINDMORE SALES COUNCIL (BSC)</h2>
      <p>The <b>BSC</b> is a by invitation only global community of high caliber Sales Professionals in the IT industry. Participating in the BSC provides significant wealth creation opportunities by earning consulting fees and sales commission or finding an exciting startup to work for.</p>
      <p><b>BSC</b> members actively collaborate with each other to close deals, generate leads &amp; opportunities, navigate through client organizations and build a true advisory status with customers.</p>
      <p><b>BSC</b> members get early first hand visibility into the latest technology innovations &amp; learn how those technologies could assist their clients in solving their complex business objectives.</p>
    </section>

    <article class="card card-how">
      <div class="card-icon"><span>
        <svg width="40" height="34" viewBox="0 0 40 34"><rect x="13" y="1" width="14" height="7" rx="2" fill="none" stroke="#fff" stroke-width="2.5"/><rect x="1" y="7" width="38" height="26" rx="3" fill="#fff"/><rect x="17" y="16" width="6" height="5" fill="#3b9ad9"/><rect x="1" y="17" width="38" height="2" fill="#3b9ad9"/></svg>
      </span></div>
      <h3><u>HOW IT WORKS</u></h3>
      <p>BSC members will be introduced to Brindmore Capital's client and portfolio companies. This unique ability to learn about latest technology innovation keeps the participants up to date with industry trends and could open interesting earning or employment opportunities.</p>
      <p>Once exposed to a specific vendor, BSC members can decide if and how they would like to get further involved. Dependent on the interest level for the specific technology, the ability to offer a solution to a known customer problem or the sheer interest to develop new business, BSC members can participate in two ways.</p>
    </article>

    <article class="card card-assoc">
      <div class="card-icon"><span>
        <svg width="44" height="40" viewBox="0 0 44 40"><g fill="none" stroke="#fff" stroke-width="2"><circle cx="22" cy="18" r="16"/><ellipse cx="22" cy="18" rx="7" ry="16"/><line x1="6" y1="18" x2="38" y2="18"/><line x1="9" y1="10" x2="35" y2="10"/></g><g fill="#fff"><circle cx="12" cy="26" r="3.5"/><circle cx="22" cy="25" r="3.5"/><circle cx="32" cy="26" r="3.5"/><rect x="7" y="31" width="10" height="8" rx="3"/><rect x="17" y="30" width="10" height="9" rx="3"/><rect x="27" y="31" width="10" height="8" rx="3"/></g></svg>
      </span></div>
      <h3><u>AS ASSOCIATES</u></h3>
      <p>Associates are actively selling and promoting one or more Brindmore Capital portfolio companies. This could be an employment or a freelance opportunity.</p>
    </article>

    <article class="card card-adv">
      <div class="card-icon"><span>
        <svg width="44" height="36" viewBox="0 0 44 36"><g fill="#fff"><circle cx="11" cy="7" r="5"/><circle cx="31" cy="7" r="5"/><rect x="5" y="13" width="12" height="12" rx="3"/><rect x="25" y="13" width="12" height="12" rx="3"/><rect x="2" y="21" width="40" height="3"/><rect x="7" y="24" width="2.5" height="11"/><rect x="34" y="24" width="2.5" height="11"/><rect x="18" y="15" width="7" height="6"/></g></svg>
      </span></div>
      <h3><u>AS ADVISORS</u></h3>
      <p>Advisors offer their contacts and knowledge about customers to Associates.<br>Advisors could create leads, support with introductions, explain customer organization and processes etc. They will be compensated by Associates with a pre-negotiated % of commission of a future sale that was supported by the Advisor.<br>Whatever level of involvement a BSC member seeks there is plenty of opportunity to be rewarded for working with fellow Sales Professionals and Great Startups on the forefront of technical innovation.</p>
    </article>

    <div class="rule"></div>

    <footer class="footer">
      <div class="office office-usa">
        <h4>USA</h4>
        <ul>
          <li><svg width="11" height="11" viewBox="0 0 12 12"><path d="M2 1l2.5 0 1 3-1.5 1a7 7 0 0 0 3 3l1-1.5 3 1V10a1 1 0 0 1-1 1A10 10 0 0 1 1 2a1 1 0 0 1 1-1z" fill="#fff"/></svg>+1-555-010 2413</li>
          <li><svg width="11" height="9" viewBox="0 0 12 9"><rect width="12" height="9" fill="#fff"/><path d="M0 0l6 5 6-5" fill="none" stroke="#1b5d9c" stroke-width="1.2"/></svg>info@brindmore.capital</li>
          <li><svg width="9" height="12" viewBox="0 0 10 13"><path d="M5 0a5 5 0 0 1 5 5c0 3-5 8-5 8S0 8 0 5a5 5 0 0 1 5-5z" fill="#fff"/><circle cx="5" cy="5" r="2" fill="#1b5d9c"/></svg>48 Harlow Ave. Fairhaven, CA 94000</li>
        </ul>
      </div>
      <div class="footer-brand">BRINDMORE CAPITAL</div>
      <div class="office office-eu">
        <h4>EUROPE</h4>
        <ul>
          <li><svg width="11" height="11" viewBox="0 0 12 12"><path d="M2 1l2.5 0 1 3-1.5 1a7 7 0 0 0 3 3l1-1.5 3 1V10a1 1 0 0 1-1 1A10 10 0 0 1 1 2a1 1 0 0 1 1-1z" fill="#fff"/></svg>+49 170 0004 188</li>
          <li><svg width="11" height="9" viewBox="0 0 12 9"><rect width="12" height="9" fill="#fff"/><path d="M0 0l6 5 6-5" fill="none" stroke="#1b5d9c" stroke-width="1.2"/></svg>info@brindmore.capital</li>
          <li><svg width="9" height="12" viewBox="0 0 10 13"><path d="M5 0a5 5 0 0 1 5 5c0 3-5 8-5 8S0 8 0 5a5 5 0 0 1 5-5z" fill="#fff"/><circle cx="5" cy="5" r="2" fill="#1b5d9c"/></svg>Lindenweg 7, 10100 Berlin - Germany</li>
        </ul>
      </div>
    </footer>
  </div>
</div>
</body>
</html>
```